Local fast-growing company in the service sector

We are looking for a modern business card design, which should also appear on our letterheads

Target Market(s)

Private and industrial sectors

Contact Information for Business Card

Vorname Name
Lindkofer Str. 18
71468 Remsbach
Tel.: 07163-418259-0
Name@kovaltec-pbz.de

Colors
9d9d9d
919191
aaaaaa

Requirements
Must have
• The logo (file) in silver

```html
<!DOCTYPE html>
<html lang="de">
<head>
<meta charset="utf-8">
<title>KOVALTEC – Visitenkarte</title>
<link rel="stylesheet" href="https://fonts.googleapis.com/css2?family=Source+Sans+3:wght@400;600&display=swap">
<style>
  :root {
    --page: #d9d7d4;
    --card: #151516;
    --card-edge: #202022;
    --silver: #aaaaaa;
    --silver-mid: #9d9d9d;
    --silver-dark: #919191;
    --text-light: #e6e6e6;
  }
  * { box-sizing: border-box; margin: 0; padding: 0; }
  html, body {
    width: 1200px; height: 864px; overflow: hidden;
    background: var(--page);
    font-family: "Source Sans 3", "Myriad Pro", sans-serif;
  }
  .stage {
    width: 1200px; height: 864px;
    display: flex; align-items: center; justify-content: center; gap: 40px;
  }
  .card {
    position: relative;
    width: 540px; height: 310px;
    background: var(--card);
    border: 1px solid var(--card-edge);
    box-shadow: 0 10px 28px rgba(0,0,0,.25);
  }

  /* Back side */
  .card--back .brand {
    position: absolute; left: 0; right: 0; top: 100px;
    display: flex; align-items: center; justify-content: center; gap: 14px;
  }
  .brand__mark {
    width: 22px; height: 22px; border-radius: 50%;
    background: var(--silver);
  }
  .brand__name {
    font-weight: 600; font-size: 46px; letter-spacing: 2px;
    color: var(--silver); line-height: 1;
  }
  .card--back .web {
    position: absolute; left: 0; right: 0; bottom: 70px; text-align: center;
    font-size: 15px; letter-spacing: 7px; color: var(--silver-dark);
  }

  /* Front side */
  .card--front .brand {
    position: absolute; left: 150px; top: 58px;
    display: flex; align-items: center; gap: 14px;
  }
  .card--front .brand__name { font-size: 48px; }
  .brand__sub {
    position: absolute; left: 186px; top: 112px;
    font-size: 17px; letter-spacing: 1px; color: var(--silver-mid);
  }
  .contact {
    position: absolute; left: 0; right: 0; top: 170px;
    display: flex; justify-content: center; align-items: stretch;
  }
  .contact__person {
    text-align: right; padding-right: 18px;
    font-size: 16px; line-height: 1.3; color: var(--text-light);
  }
  .contact__name {
    font-weight: 600; color: var(--silver-mid); letter-spacing: .5px;
  }
  .contact__divider { width: 1px; background: var(--silver-dark); }
  .contact__lines {
    list-style: none; padding-left: 18px;
    font-size: 16px; line-height: 1.3; color: var(--text-light);
  }
  .contact__lines li { display: flex; align-items: center; gap: 8px; }
  .contact__lines svg { width: 12px; height: 12px; fill: var(--silver); flex: none; }
</style>
</head>
<body>
<main class="stage">
  <section class="card card--back" aria-label="Kartenrückseite">
    <div class="brand">
      <span class="brand__mark"></span>
      <span class="brand__name">KOVALTEC</span>
    </div>
    <p class="web">www.kovaltec-pbz.de</p>
  </section>

  <section class="card card--front" aria-label="Kartenvorderseite">
    <div class="brand">
      <span class="brand__mark"></span>
      <span class="brand__name">KOVALTEC</span>
    </div>
    <p class="brand__sub">kovaltec-pbz.de</p>

    <div class="contact">
      <div class="contact__person">
        <p class="contact__name">LENA HARTWIG</p>
        <p>Lindkofer Str. 18</p>
        <p>71468 Remsbach</p>
      </div>
      <div class="contact__divider"></div>
      <ul class="contact__lines">
        <li>
          <svg viewBox="0 0 12 12" aria-hidden="true"><path d="M2.5 1h2l1 3-1.5 1a6 6 0 0 0 3 3l1-1.5 3 1v2c0 .8-.7 1.5-1.5 1.5A9.5 9.5 0 0 1 1 2.5C1 1.7 1.7 1 2.5 1z"/></svg>
          07163-418259-0
        </li>
        <li>
          <svg viewBox="0 0 12 12" aria-hidden="true"><path d="M1 2.5h10v7H1z M1.5 3 6 6.5 10.5 3" stroke="#151516" stroke-width=".8"/></svg>
          lena@kovaltec-pbz.de
        </li>
        <li>
          <svg viewBox="0 0 12 12" aria-hidden="true"><circle cx="6" cy="6" r="5"/><path d="M1 6h10M6 1c-2.5 3-2.5 7 0 10M6 1c2.5 3 2.5 7 0 10" stroke="#151516" stroke-width=".8" fill="none"/></svg>
          www.kovaltec-pbz.de
        </li>
      </ul>
    </div>
  </section>
</main>
</body>
</html>
```